Brochure Design Project

I am looking for a trifold brochure.
I would like it to be square (5.5 x 5.5)
The back needs to be reserved for a map and logo information.

we are a financial planning firm. we have been in operation for 15 years.
our clients are ecstatic and continue to refer others to us.

Brochure COPY:
Building Wealth, Building Futures
We start with your goals. Then we build a comprehensive strategy to manage your investments, grow your wealth, minimize your tax burden and protect your family. Most importantly, we keep you informed about market change, opportunities and concerns before they impact you, so you can make confident decisions about your future, every step of the way.

Understanding and Expertise (bios)
Steadfast Money Partners is led by Lorna Feldskov and Miriam Oakhurst, experienced business partners who take the time to listen to you, understand your needs and present you with all your options.
Our focus in on your future, and building a confident and financially secure path for you and your family for the years ahead.

Lorna Feldskov, BSc, MBA, CPA, CA, CFP, FMA, CPCA
Certified Financial Planner

With years of experience in tax, investment, estate and retirement issues - and an extensive business background - Lorna provided her clients with important financial insights and clear direction in a friendly and open manner.

Miriam Oakhurst, BSEd, FMA, CPCA, CFP, FCSI, CIM

After a successful tennis career Miriam joined Lorna in the financial industry. Miriam quickly discovered how much she enjoys working with people and helping them to achieve their goals. Leveraging the discipline and work ethic developed during her tennis career, Miriam has been instrumental in creating the successful process used by Steadfast Money Partners.

People Trust Us to Help Them
The important things in life are often neglected due to the demands of day to day, including financial planning and wealth management. But it doesn't have to be that way when you have a trustworthy team looking out for you.
At Steadfast Money Partners we have the knowledge, experience and resources to help you move forward and realize your financial goals.

(side note) on the back of the brochure it should have the SMP logo, the office address, 382 Kettlewood Rd. E. Mississauga, ON L5R 7M4, and our website address.

Reason: Am juggling a number of different projects so need to extend the deadline on this one. Will provide copy for the project by end of day today.

Target Market(s)

We would like the brochure to appeal to the high net worth client who is currently working with an advisor but is not getting the attention from them.

Industry/Entity Type

Financial

Requirements
Must have
• SMP Logo on the front. The logo is blue with black font and has a tagline with it that says "Choose your path, change your future."
you can see the logo at www.plantharvestsoon.ca

One page must be about the two advisors, Lorna Feldskov and Miriam Oakhurst.
(leave an open area for bios and we will fill it in)

We want it to talk about building wealth and passing it on to the next generation.
Should not have
• Financial lingo.

```html
<!DOCTYPE html>
<html lang="en">
<head>
<meta charset="utf-8">
<title>Steadfast Money Partners – Trifold Brochure Inside Spread</title>
<link rel="stylesheet" href="https://fonts.googleapis.com/css2?family=Advent+Pro:wght@400;500;600&display=swap">
<style>
  :root {
    --canvas-grey: #e4e4e4;
    --brand-blue: #1b8bd8;
    --heading-white: #ffffff;
    --body-ink: #1a2b3f;
    --photo-divider: #ffffff;
  }
  * { box-sizing: border-box; margin: 0; padding: 0; }
  html, body {
    width: 1200px; height: 400px; overflow: hidden;
    background: var(--canvas-grey);
  }
  .spread { position: relative; width: 1200px; height: 400px; }
  .panel {
    position: absolute; top: 15px; width: 367px; height: 368px;
    background: var(--brand-blue); overflow: hidden;
  }
  .panel--wealth { left: 17px; }
  .panel--bios { left: 416px; }
  .panel--trust { left: 816px; }

  .photo { position: absolute; display: block; }

  .heading {
    position: absolute;
    font-family: "Advent Pro", sans-serif;
    font-weight: 500; font-size: 15.5px; line-height: 18px;
    color: var(--heading-white); white-space: nowrap;
  }
  .copy {
    position: absolute;
    font-family: "Advent Pro", sans-serif;
    font-weight: 500; font-size: 10.6px; line-height: 11.7px;
    color: var(--body-ink); text-align: justify;
  }
  .copy p + p { margin-top: 5px; }

  /* Panel 1 */
  .panel--wealth .photo-estate {
    left: 0; top: 0; width: 367px; height: 185px;
    background: linear-gradient(180deg, #7a4b6e 0%, #d98a4a 30%, #b8653a 55%, #4a2a1c 78%, #2b4a5e 100%);
  }
  .panel--wealth .heading { left: 27px; top: 206px; }
  .panel--wealth .copy { left: 133px; top: 232px; width: 214px; }

  /* Panel 2 */
  .photo-column { position: absolute; left: 0; top: 0; width: 146px; height: 368px; background: var(--photo-divider); }
  .photo-savings { left: 0; top: 0; width: 146px; height: 91px;
    background: linear-gradient(135deg, #f4f4f4 0%, #eab7c8 55%, #f1f1f1 100%); }
  .photo-couple { left: 0; top: 93px; width: 146px; height: 91px;
    background: linear-gradient(135deg, #e9e6e3 0%, #d9b9a9 45%, #8fb0c9 75%, #ededed 100%); }
  .photo-home { left: 0; top: 186px; width: 146px; height: 90px;
    background: linear-gradient(180deg, #b9c9d6 0%, #8a7866 45%, #5d7a45 80%, #4c6a38 100%); }
  .photo-meeting { left: 0; top: 278px; width: 146px; height: 90px;
    background: linear-gradient(135deg, #e8e1d6 0%, #c9b49c 45%, #2e2e36 75%, #ded8ce 100%); }
  .panel--bios .heading { left: 159px; top: 25px; }
  .panel--bios .copy { left: 159px; top: 48px; width: 196px; }

  /* Panel 3 */
  .panel--trust .copy--intro { left: 17px; top: 25px; width: 335px; }
  .panel--trust .heading { left: 17px; top: 120px; }
  .panel--trust .copy--trust { left: 17px; top: 141px; width: 335px; }
  .panel--trust .photo-golf {
    left: 95px; top: 253px; width: 184px; height: 115px;
    background: linear-gradient(180deg, #7fb2dd 0%, #c6dcee 40%, #3d5f8f 70%, #1f3d6d 100%);
  }
</style>
</head>
<body>
<main class="spread">

  <section class="panel panel--wealth">
    <div class="photo photo-estate" role="img" aria-label="Photo of a large luxury home with a pool at sunset"></div>
    <h2 class="heading">Building Wealth, Building Futures</h2>
    <div class="copy">
      <p>We start with your goals. Then we build a comprehensive strategy to manage your investments, grow your wealth, minimize your tax burden and protect your family. Most importantly, we keep you informed about market change, opportunities and concerns before they impact you, so you can make confident decisions about your future, every step of the way.</p>
    </div>
  </section>

  <section class="panel panel--bios">
    <div class="photo-column">
      <div class="photo photo-savings" role="img" aria-label="Photo of a coin dropped into a pink piggy bank"></div>
      <div class="photo photo-couple" role="img" aria-label="Photo of a young couple reviewing finances with an advisor"></div>
      <div class="photo photo-home" role="img" aria-label="Photo of a suburban family house"></div>
      <div class="photo photo-meeting" role="img" aria-label="Photo of an advisor shaking hands with a senior couple"></div>
    </div>
    <h2 class="heading">Understanding and expertise (bios)</h2>
    <div class="copy">
      <p>Steadfast Money Partners is led by Lorna Feldskov and Miriam Oakhurst, experienced business partners who take the time to listen to you, understand your needs and present you with all your options.</p>
      <p>Our focus in on your future, and building a confident and financially secure path for you and your family for the years ahead.</p>
      <p>Lorna Feldskov, BSc, MBA, CPA, CA, CFP, FMA, CPCA<br>Certified Financial Planner</p>
      <p>With years of experience in tax, investment, estate and retirement issues - and an extensive business background - Lorna provided her clients with important financial insights and clear direction in a friendly and open manner.</p>
      <p>Miriam Oakhurst, BSEd, FMA, CPCA, CFP, FCSI, CIM Certified Financial Planner</p>
    </div>
  </section>

  <section class="panel panel--trust">
    <div class="copy copy--intro">
      <p>After a successful tennis career Miriam joined Lorna in the financial industry. Miriam quickly discovered how much she enjoys working with people and helping them to achieve their goals. Leveraging the discipline and work ethic developed during her tennis career, Miriam has been instrumental in creating the successful process used by Steadfast Money Partners.</p>
    </div>
    <h2 class="heading">People Trust Us to Help Them</h2>
    <div class="copy copy--trust">
      <p>The important things in life are often neglected due to the demands of day to day, including financial planning and wealth management. But it doesn't have to be that way when you have a trustworthy team looking out for you.</p>
      <p>At Steadfast Money Partners we have the knowledge, experience and resources to help you move forward and realize your financial goals.</p>
    </div>
    <div class="photo photo-golf" role="img" aria-label="Photo of a golfer mid-swing against a blue sky"></div>
  </section>

</main>
</body>
</html>
```